Business Card Design for new logo

Business card Design for new logo. Follow colors from logo.
The company has offices in multiple comtries
Want to have some bulltes on the countries and also on the main services

Something like
USA*Dominican Republic*LATAM

Consulting*Healthcare IT*Tranformation

Industry/Entity Type

Information Technology

Contact Information for Business Card

Address, Phones, countries, name and position

Miron castell

Founder and CEO

947 Quarry Ln
Mill haven, PA 16835

Mcastell@novelquin.com

www.novelquin.com

717-352-6081

828-444-4444

```html
<!DOCTYPE html>
<html lang="en">
<head>
<meta charset="utf-8">
<title>Novelquin Business Card</title>
<link rel="stylesheet" href="https://fonts.googleapis.com/css2?family=Marcellus&family=Open+Sans:wght@400;600;700&display=swap">
<style>
  :root {
    --backdrop: #dfe3e5;
    --brand-blue: #2673b3;
    --brand-orange: #f28a4f;
    --card-white: #ffffff;
    --ink-blue: #2166ac;
  }
  * { box-sizing: border-box; margin: 0; padding: 0; }
  html, body {
    width: 1200px;
    height: 1000px;
    overflow: hidden;
    background: var(--backdrop);
    font-family: "Open Sans", Arial, sans-serif;
  }
  .card {
    position: absolute;
    left: 236px;
    border-radius: 30px;
    overflow: hidden;
  }
  .card-front {
    top: 50px;
    width: 730px;
    height: 387px;
    background: var(--brand-blue);
  }
  .front-mark {
    position: absolute;
    left: 50%;
    top: 80px;
    width: 100px;
    height: 100px;
    margin-left: -50px;
    border-radius: 50%;
    background: var(--brand-orange);
  }
  .front-name {
    position: absolute;
    left: 0;
    right: 0;
    top: 222px;
    text-align: center;
    font-family: "Marcellus", Georgia, serif;
    font-size: 76px;
    line-height: 1;
    color: var(--card-white);
  }
  .front-countries {
    position: absolute;
    left: 0;
    right: 0;
    top: 322px;
    text-align: center;
    font-size: 19px;
    font-weight: 600;
    letter-spacing: 0.5px;
    color: var(--card-white);
  }
  .bullet { color: var(--brand-orange); margin: 0 10px; }
  .card-back {
    top: 552px;
    width: 726px;
    height: 380px;
    background: var(--card-white);
  }
  .person-name {
    position: absolute;
    left: 49px;
    top: 34px;
    font-size: 28px;
    font-weight: 700;
    color: var(--ink-blue);
  }
  .person-role {
    position: absolute;
    left: 49px;
    top: 72px;
    font-size: 19px;
    color: var(--brand-orange);
  }
  .service-line {
    position: absolute;
    left: 49px;
    top: 106px;
    font-size: 15px;
    font-weight: 600;
    color: var(--ink-blue);
  }
  .service-line .bullet { margin: 0 6px; }
  .contact-list {
    position: absolute;
    left: 47px;
    top: 148px;
    list-style: none;
    color: var(--ink-blue);
    font-size: 19px;
    line-height: 26px;
  }
  .contact-item {
    display: flex;
    align-items: flex-start;
    margin-bottom: 9px;
  }
  .contact-icon {
    width: 22px;
    height: 22px;
    margin: 2px 11px 0 0;
    flex: none;
    fill: var(--brand-orange);
  }
  .brand-area {
    position: absolute;
    left: 380px;
    top: 20px;
    width: 325px;
    height: 345px;
  }
  .brand-dot {
    position: absolute;
    left: 50%;
    top: 60px;
    width: 140px;
    height: 140px;
    margin-left: -70px;
    border-radius: 50%;
    background: var(--brand-orange);
  }
  .brand-name {
    position: absolute;
    left: 0;
    right: 0;
    top: 230px;
    text-align: center;
    font-family: "Marcellus", Georgia, serif;
    font-size: 50px;
    line-height: 1;
    color: var(--brand-blue);
  }
</style>
</head>
<body>

<section class="card card-front">
  <div class="front-mark"></div>
  <div class="front-name">Novelquin</div>
  <p class="front-countries">USA<span class="bullet">&#9679;</span>Dominican Republic<span class="bullet">&#9679;</span>LATAM</p>
</section>

<section class="card card-back">
  <h1 class="person-name">Miron castell</h1>
  <p class="person-role">Founder and CEO</p>
  <p class="service-line">Consulting<span class="bullet">&#9679;</span>Healthcare IT<span class="bullet">&#9679;</span>Transformation</p>

  <ul class="contact-list">
    <li class="contact-item">
      <svg class="contact-icon" viewBox="0 0 24 24" aria-hidden="true"><path d="M6.6 10.8a15.1 15.1 0 0 0 6.6 6.6l2.2-2.2a1 1 0 0 1 1-.25 11.4 11.4 0 0 0 3.6.57 1 1 0 0 1 1 1V20a1 1 0 0 1-1 1A17 17 0 0 1 3 4a1 1 0 0 1 1-1h3.5a1 1 0 0 1 1 1c0 1.25.2 2.45.57 3.57a1 1 0 0 1-.25 1z"/></svg>
      <span>717-352-6081<br>828-444-4444</span>
    </li>
    <li class="contact-item">
      <svg class="contact-icon" viewBox="0 0 24 24" aria-hidden="true"><path d="M2 6h20v12H2z M3 7l9 6 9-6" fill="none" stroke="#f28a4f" stroke-width="2"/><path d="M2 6h20L12 13z"/></svg>
      <span>Mcastell@novelquin.com</span>
    </li>
    <li class="contact-item">
      <svg class="contact-icon" viewBox="0 0 24 24" aria-hidden="true"><g fill="none" stroke="#f28a4f" stroke-width="1.6"><circle cx="12" cy="12" r="9.5"/><ellipse cx="12" cy="12" rx="4.2" ry="9.5"/><path d="M2.5 12h19M4 7h16M4 17h16"/></g></svg>
      <span>www.novelquin.com</span>
    </li>
    <li class="contact-item">
      <svg class="contact-icon" viewBox="0 0 24 24" aria-hidden="true"><path d="M12 1.5a7.5 7.5 0 0 0-7.5 7.5c0 5.6 7.5 13.5 7.5 13.5s7.5-7.9 7.5-13.5A7.5 7.5 0 0 0 12 1.5zm0 10.3a2.8 2.8 0 1 1 0-5.6 2.8 2.8 0 0 1 0 5.6z"/></svg>
      <span>947 Quarry Ln<br>Mill haven, PA 16835</span>
    </li>
  </ul>

  <div class="brand-area">
    <div class="brand-dot"></div>
    <div class="brand-name">Novelquin</div>
  </div>
</section>

</body>
</html>
```